Northern Falcon 250 Poster Design

Poster for the Public to draw them to the Event
- Northern Falcon 250. Largest Prize Money Race in Western Canada to Late Model Racing. Driver Competing for $65,000 in Prize Money Featuring Late Models and Street Stock Racers from Canada and the U.S. Don't miss the Inaugural Northern Falcon 250 at the Newly renovated Marlowe Raceway .
-Marlowe Raceway Address 1845 Quillan Road
- April 29th -30th
- Gates Open and 4:30 pm Racing starts at 5 pm
- Adults $20
- Youth 12-17 $15
- Senior $15
- Under 12 Free

This is a major event and the newly renovated Marlowe Raceway that will attract racers from many cities and Kick off the 2022 racing Season

Low design quality

Target Market(s)

Fans

Industry/Entity Type

Autombobile race

Requirements
Must have
• Dates, times, logo, address, cars
Nice to have
• Clear bold Dates, draws the eyes, cool car pictures of Asphalt Late Model Race Cars

```html
<!DOCTYPE html>
<html lang="en">
<head>
<meta charset="utf-8">
<title>Northern Falcon 250 – Marlowe Raceway</title>
<link rel="stylesheet" href="https://fonts.googleapis.com/css2?family=Anton&family=Alfa+Slab+One&family=Oswald:wght@500&family=Montserrat:wght@400;600;700&display=swap">
<style>
  :root{
    --ink:#2a2727;
    --ink-soft:#353131;
    --yellow:#f0c419;
    --yellow-deep:#d9a90f;
    --gold:#b8912a;
    --grey:#8f8f8f;
    --white:#ffffff;
    --black:#121111;
  }
  *{margin:0;padding:0;box-sizing:border-box}
  html,body{width:874px;height:1200px;overflow:hidden;background:var(--ink)}
  .poster{position:relative;width:874px;height:1200px;background:var(--ink);overflow:hidden;font-family:"Montserrat",sans-serif;color:var(--white)}
  .backdrop-word{position:absolute;top:80px;left:0;width:100%;text-align:center;font-family:"Montserrat",sans-serif;font-weight:700;font-size:130px;letter-spacing:14px;color:var(--ink-soft)}
  .brand{position:absolute;top:150px;left:0;width:100%;display:flex;justify-content:center;align-items:center;gap:12px}
  .brand-dot{width:22px;height:22px;border-radius:50%;background:var(--yellow)}
  .brand-name{font-family:"Montserrat",sans-serif;font-weight:700;font-size:26px;letter-spacing:3px;color:var(--white)}
  .title-band{position:absolute;top:266px;left:0;width:100%;height:100px;background:var(--yellow);border-bottom:3px solid var(--yellow-deep);display:flex;align-items:center;justify-content:center}
  .title{font-family:"Anton",sans-serif;font-size:76px;line-height:1;color:var(--black);letter-spacing:1px}
  .hero{position:absolute;top:366px;left:0;width:874px;height:540px}
  .hero-text{position:absolute;top:380px;left:0;width:100%;text-align:center}
  .tagline{font-family:"Alfa Slab One",serif;font-size:35px;color:var(--ink);line-height:1.1}
  .tagline-sub{font-family:"Montserrat",sans-serif;font-size:18px;font-weight:600;color:var(--ink);letter-spacing:1px;margin-top:4px}
  .date{position:absolute;top:870px;left:0;width:100%;text-align:center;font-family:"Anton",sans-serif;font-size:76px;line-height:1;color:var(--white)}
  .times{position:absolute;top:962px;left:0;width:100%;text-align:center;font-family:"Oswald",sans-serif;font-weight:500;font-size:26px;color:var(--yellow)}
  .times .divider{margin:0 10px}
  .details{position:absolute;top:1022px;left:90px;width:694px;text-align:center;font-size:11.5px;line-height:1.35}
  .details b{font-weight:700}
  .address-band{position:absolute;top:1064px;left:87px;width:699px;height:32px;background:var(--grey);display:flex;align-items:center;justify-content:center;font-family:"Alfa Slab One",serif;font-size:20px;letter-spacing:1.5px;color:var(--white)}
  .price-band{position:absolute;top:1098px;left:87px;width:699px;height:66px;background:var(--yellow);display:flex;align-items:center;justify-content:space-around;padding:0 14px;font-family:"Anton",sans-serif;font-size:19px;color:var(--ink)}
  .cone{width:26px;height:32px}
</style>
</head>
<body>
<main class="poster">
  <div class="backdrop-word" aria-hidden="true">MARLOWE</div>

  <header class="brand">
    <span class="brand-dot"></span>
    <span class="brand-name">MARLOWE RACEWAY</span>
  </header>

  <section class="title-band">
    <h1 class="title">NORTHERN FALCON 250</h1>
  </section>

  <svg class="hero" viewBox="0 0 874 540" aria-hidden="false">
    <defs>
      <linearGradient id="heroFill" x1="0" y1="0" x2="0" y2="1">
        <stop offset="0" stop-color="#c9a83a"/>
        <stop offset="0.22" stop-color="#8f8a7a"/>
        <stop offset="0.55" stop-color="#5a5d78"/>
        <stop offset="1" stop-color="#1c1b22"/>
      </linearGradient>
      <linearGradient id="heroSide" x1="0" y1="0" x2="1" y2="0">
        <stop offset="0" stop-color="#b0333a" stop-opacity="0.45"/>
        <stop offset="0.5" stop-color="#000" stop-opacity="0"/>
        <stop offset="1" stop-color="#d83a2a" stop-opacity="0.4"/>
      </linearGradient>
    </defs>
    <g role="img" aria-label="Photo of late model race cars battling on an asphalt oval track">
      <path d="M0 0 H874 V442 Q620 500 437 530 Q240 500 0 445 Z" fill="url(#heroFill)"/>
      <path d="M0 0 H874 V442 Q620 500 437 530 Q240 500 0 445 Z" fill="url(#heroSide)"/>
    </g>
    <path d="M0 445 Q240 500 437 530 Q620 500 874 442" fill="none" stroke="var(--gold)" stroke-width="4"/>
  </svg>

  <div class="hero-text">
    <p class="tagline">LARGEST PRIZE MONEY RACE</p>
    <p class="tagline-sub">IN WESTERN CANADA TO LATE MODEL RACING</p>
  </div>

  <svg style="position:absolute;top:0;left:0" width="874" height="1200" aria-hidden="true">
    <g fill="var(--white)">
      <polygon points="0,832 40,852 40,890 0,870"/>
      <polygon points="40,890 80,910 80,948 40,928"/>
      <polygon points="0,910 40,930 40,968 0,948"/>
      <polygon points="874,790 874,830 834,852 834,812"/>
      <polygon points="834,852 834,892 794,914 794,874"/>
      <polygon points="874,870 874,910 834,932 834,892"/>
    </g>
  </svg>

  <h2 class="date">APRIL 29TH -30TH</h2>
  <p class="times">GATES OPEN 4:30 PM<span class="divider">|</span>RACING STARTS AT 5 PM</p>
  <p class="details">Driver Competing for <b>$65,000</b> in Prize Money Featuring <b>Late Models and Street Stock Racers</b> from Canada and the U.S. Don't miss the Inaugural Northern Falcon 250 at the Newly renovated Marlowe Raceway .</p>

  <div class="address-band">MARLOWE RACEWAY ADDRESS 1845 QUILLAN ROAD</div>

  <div class="price-band">
    <span>ADULTS $20</span>
    <svg class="cone" viewBox="0 0 26 32" aria-hidden="true"><polygon points="13,2 21,27 5,27" fill="#f26a1b"/><rect x="8" y="11" width="10" height="3" fill="#fff"/><rect x="6.5" y="18" width="13" height="3" fill="#fff"/><rect x="2" y="27" width="22" height="3" fill="#c44d12"/></svg>
    <span>YOUTH 12-17 $15</span>
    <svg class="cone" viewBox="0 0 26 32" aria-hidden="true"><polygon points="13,2 21,27 5,27" fill="#f26a1b"/><rect x="8" y="11" width="10" height="3" fill="#fff"/><rect x="6.5" y="18" width="13" height="3" fill="#fff"/><rect x="2" y="27" width="22" height="3" fill="#c44d12"/></svg>
    <span>SENIOR $15</span>
    <svg class="cone" viewBox="0 0 26 32" aria-hidden="true"><polygon points="13,2 21,27 5,27" fill="#f26a1b"/><rect x="8" y="11" width="10" height="3" fill="#fff"/><rect x="6.5" y="18" width="13" height="3" fill="#fff"/><rect x="2" y="27" width="22" height="3" fill="#c44d12"/></svg>
    <span>UNDER 12 FREE</span>
  </div>
</main>
</body>
</html>
```